Real Estate Flyer

I would like an A4 size flyer which has the same info 3 times and can be cut into three.
It will be used for letterbox drops for new listings (SELLING) and sold listings (SOLD). The flyer needs a heading (as above) and a space for a photo which is able to be changed for each new property. Needs to be blue, red and white. It also requires my photo, KLV logo, Marisska Thornbury logo and the following text:
"Are you considering selling? Call Marisska today for a complimentary market appraisal".
(KLV logo, Marisska Thornbury Sales Consultant logo and my photo can be found in uploaded files)

```html
<!DOCTYPE html>
<html lang="en">
<head>
<meta charset="utf-8">
<title>KLV Selling Flyer</title>
<link href="https://fonts.googleapis.com/css2?family=Arimo:wght@400;700&family=Questrial&display=swap" rel="stylesheet">
<style>
  :root {
    --red: #ec1c24;
    --blue: #2b3a86;
    --white: #ffffff;
    --grey: #6d6e71;
    --photo-top: #c9d6e6;
    --photo-bottom: #8a8676;
    --portrait-top: #7a6a62;
    --portrait-bottom: #3a3340;
  }
  html, body {
    margin: 0;
    padding: 0;
    width: 1200px;
    height: 2468px;
    overflow: hidden;
    background: var(--white);
  }
  .flyer {
    position: relative;
    width: 1200px;
    height: 2468px;
    font-family: "Arimo", Arial, sans-serif;
  }
  .flyer > * { position: absolute; box-sizing: border-box; }

  .brand-square {
    left: 120px; top: 92px; width: 144px; height: 144px;
    background: var(--blue);
  }
  .brand-name {
    left: 292px; top: 88px; height: 152px;
    margin: 0;
    color: var(--blue);
    font-weight: 700;
    font-size: 120px;
    line-height: 152px;
  }
  .headline {
    left: 120px; top: 236px; width: 968px;
    margin: 0;
    color: var(--red);
    font-weight: 700;
    font-size: 228px;
    line-height: 220px;
    letter-spacing: -4px;
    text-align: center;
  }

  .feature-panel {
    left: 120px; top: 472px; width: 968px; height: 648px;
    background: var(--red);
  }
  .feature-photo {
    left: 216px; top: 500px; width: 776px; height: 420px;
    border: 6px solid var(--blue);
    background: linear-gradient(180deg, var(--photo-top), var(--photo-bottom));
  }
  .address-box {
    left: 216px; top: 960px; width: 776px; height: 112px;
    border: 5px solid var(--white);
  }

  .info-panel {
    left: 120px; top: 1120px; width: 968px; height: 780px;
    background: var(--blue);
  }
  .gallery-photo {
    top: 1160px; width: 410px; height: 320px;
    border: 6px solid var(--white);
    background: linear-gradient(180deg, var(--photo-top), var(--photo-bottom));
  }
  .gallery-photo.first { left: 140px; }
  .gallery-photo.second { left: 600px; }

  .question {
    left: 134px; top: 1508px; width: 950px;
    margin: 0;
    color: var(--white);
    font-size: 96px;
    line-height: 104px;
    font-weight: 400;
  }
  .call-to-action {
    left: 134px; top: 1742px; width: 950px;
    margin: 0;
    color: var(--white);
    font-size: 52px;
    line-height: 66px;
  }

  .agent-portrait {
    left: 120px; top: 1916px; width: 272px; height: 386px;
    border: 5px solid var(--blue);
    background: linear-gradient(180deg, var(--portrait-top), var(--portrait-bottom));
  }
  .agent-card {
    left: 392px; top: 1916px; width: 696px; height: 386px;
    border: 5px solid var(--red);
    font-family: "Questrial", "Century Gothic", sans-serif;
  }
  .agent-name {
    position: absolute; left: 28px; top: 36px;
    margin: 0;
    font-size: 66px;
    line-height: 76px;
    font-weight: 400;
    color: #111;
    letter-spacing: 2px;
  }
  .agent-mark {
    position: absolute; left: 30px; top: 172px;
    width: 140px; height: 140px;
    border-radius: 50%;
    background: #b7b8ba;
  }
  .agent-role {
    position: absolute; left: 150px; top: 126px;
    margin: 0;
    font-size: 46px;
    line-height: 54px;
    color: var(--grey);
    letter-spacing: 2px;
  }
  .agent-phone {
    position: absolute; left: 210px; top: 190px;
    margin: 0;
    font-size: 44px;
    line-height: 52px;
    color: var(--red);
    font-family: "Arimo", Arial, sans-serif;
  }
</style>
</head>
<body>
<main class="flyer">
  <div class="brand-square"></div>
  <p class="brand-name">KLV</p>
  <h1 class="headline">SELLING</h1>

  <div class="feature-panel"></div>
  <div class="feature-photo" role="img" aria-label="Photo of the featured two-storey brick house with double garage"></div>
  <div class="address-box"></div>

  <div class="info-panel"></div>
  <div class="gallery-photo first" role="img" aria-label="Photo of a listed brick family home"></div>
  <div class="gallery-photo second" role="img" aria-label="Photo of another listed brick family home"></div>

  <h2 class="question">Are you considering selling?</h2>
  <p class="call-to-action">Call Marisska today<br>for a complimentary market appraisal.</p>

  <div class="agent-portrait" role="img" aria-label="Portrait photo of sales consultant Marisska Thornbury"></div>
  <div class="agent-card">
    <p class="agent-name">Marisska Thornbury</p>
    <div class="agent-mark"></div>
    <p class="agent-role">Sales Consultant</p>
    <p class="agent-phone">0400 123 456</p>
  </div>
</main>
</body>
</html>
```